Reefline Aquaria Tropical Fish Startup Design

I need professional business cards and social media profiles for our tropical fish shop.

Target Market(s)

Tropical fish enthusiasts

Industry/Entity Type

Tropical Fish

Font styles to use
Sans Serif
Script
Other font styles liked:
• Comforta

Colors
0054AA
0677BA
7BADD7
CADEEF
E8F1F8
0094D4
00A9DD
6FCCEA
C7EBF8
E9F6FB
00AB8E
00BBA5
67D7C9
C6EFE9
E9F9F6

Requirements
Must have
• fish, oceanic colors
Nice to have
• Lines, boxes, anything that groups the title to stand out
Should not have
• Any punctuations

```html
<!DOCTYPE html>
<html lang="en">
<head>
<meta charset="utf-8">
<title>Reefline Aquaria Business Cards</title>
<link href="https://fonts.googleapis.com/css2?family=Arimo:wght@400;700&display=swap" rel="stylesheet">
<style>
  :root {
    --backdrop: #e4e4e2;
    --card: #2a2b2d;
    --card-shade: #252628;
    --teal: #17b48f;
    --text-light: #dcdcdc;
    --rule: #bdbdbd;
  }
  * { margin: 0; padding: 0; box-sizing: border-box; }
  html, body {
    width: 1200px; height: 801px; overflow: hidden;
    background: var(--backdrop);
    font-family: "Arimo", Arial, sans-serif;
  }
  .stage {
    position: relative; width: 1200px; height: 801px;
  }
  .card {
    position: absolute; top: 252px;
    width: 520px; height: 297px;
    background: var(--card);
    box-shadow: 0 4px 14px rgba(0,0,0,0.25);
    overflow: hidden;
  }
  .card--front { left: 40px; }
  .card--back { left: 640px; background: linear-gradient(100deg, var(--card-shade), var(--card) 55%, var(--card-shade)); }

  .brand-name {
    position: absolute;
    font-weight: 700;
    color: var(--teal);
    white-space: nowrap;
    letter-spacing: 0.5px;
  }
  .card--front .brand-name { top: 58px; left: 200px; font-size: 30px; }
  .card--back .brand-name { top: 126px; left: 0; width: 100%; text-align: center; font-size: 40px; }

  .address {
    position: absolute; right: 34px; top: 120px;
    text-align: right; color: var(--text-light);
    font-size: 12px; line-height: 1.35;
  }
  .person { position: absolute; left: 40px; top: 140px; }
  .person__name { color: var(--teal); font-weight: 700; font-size: 17px; letter-spacing: 0.4px; }
  .person__role { color: var(--text-light); font-size: 12px; margin-top: 2px; }

  .divider {
    position: absolute; left: 40px; right: 34px; top: 183px;
    height: 1px; background: var(--rule);
  }
  .contacts { position: absolute; left: 40px; top: 198px; list-style: none; }
  .contacts li {
    display: flex; align-items: center; gap: 9px;
    color: var(--text-light); font-size: 13px; line-height: 1; margin-bottom: 9px;
  }
  .contacts svg { width: 12px; height: 12px; flex: none; }
</style>
</head>
<body>
<main class="stage">
  <section class="card card--front" aria-label="Business card front">
    <p class="brand-name">Reefline Aquaria</p>
    <p class="address">Your address<br>city state ZIP 0000</p>
    <div class="person">
      <p class="person__name">MARCUS HALE</p>
      <p class="person__role">Manager</p>
    </div>
    <div class="divider"></div>
    <ul class="contacts">
      <li>
        <svg viewBox="0 0 12 12" aria-hidden="true"><circle cx="6" cy="6" r="6" fill="var(--teal)"/><path d="M3.8 3.2l1.2 1.4-.6.8a4 4 0 0 0 2.2 2.2l.8-.6 1.4 1.2-.8 1a5.5 5.5 0 0 1-5-5z" fill="var(--card)"/></svg>
        123-456-7800
      </li>
      <li>
        <svg viewBox="0 0 12 12" aria-hidden="true"><rect x="0.5" y="2" width="11" height="8" fill="var(--teal)"/><path d="M0.5 2l5.5 4.5L11.5 2" fill="none" stroke="var(--card)" stroke-width="1"/></svg>
        hello@reeflinemail.com
      </li>
      <li>
        <svg viewBox="0 0 12 12" aria-hidden="true"><circle cx="6" cy="6" r="6" fill="var(--teal)"/><path d="M1 6h10M6 1c-2 2.5-2 7.5 0 10M6 1c2 2.5 2 7.5 0 10" fill="none" stroke="var(--card)" stroke-width="0.8"/></svg>
        www.reeflineaquaria.com
      </li>
    </ul>
  </section>

  <section class="card card--back" aria-label="Business card back">
    <p class="brand-name">Reefline Aquaria</p>
  </section>
</main>
</body>
</html>
```